Ad design for a macarons brand

We are a dessert brand with one product line: macarons. Our products delight. Every bite is a dream!

We are launching a new product and would like to lunch a small tactical campaign for the product to boost sales.

The new macron is mango ganache and the middle a mix of sour mango and yuzu (https://www.plumvetra.com/what-is-yuzu-481630).

Here are some images we took of the new macaron
https://www.farnlooq.com/sh/tqzp8mwrhkd2aly/QWXeLpTn-vyRsdfKuJmNoP3Zt?dl=0

I attach the brand guideline document.

Required sizes

1080 x 1350
1080 x 1920

```html
<!DOCTYPE html>
<html lang="en">
<head>
<meta charset="utf-8">
<title>Lunette Macarons – Campaign Ads</title>
<link rel="stylesheet" href="https://fonts.googleapis.com/css2?family=Marcellus&family=Montserrat:wght@400;700;800&family=Bodoni+Moda:wght@500&display=swap">
<style>
  :root {
    --stage: #e6e6e6;
    --coral: #f26e5f;
    --sun: #fdbe10;
    --white: #ffffff;
    --photo-light: #f4efe8;
    --photo-warm: #f3a93a;
    --photo-deep: #e08a22;
  }
  html, body {
    margin: 0;
    width: 1200px;
    height: 1200px;
    overflow: hidden;
    background: var(--stage);
  }
  .canvas { position: relative; width: 1200px; height: 1200px; }
  .ad { position: absolute; display: block; }
  .ad--story { left: 90px; top: 167px; width: 486px; height: 864px; }
  .ad--portrait { left: 624px; top: 355px; width: 486px; height: 608px; }
  .ad__bg { fill: var(--coral); }
  .ad__dot { fill: var(--sun); }
  .ad__line { fill: none; stroke: var(--white); stroke-width: 2; opacity: .55; }
  .ad__ring { fill: none; stroke: var(--white); stroke-width: 3; }
  .brand-name { font-family: "Marcellus", serif; fill: var(--white); letter-spacing: 2px; }
  .headline { font-family: "Montserrat", sans-serif; font-weight: 800; fill: var(--white); }
  .subline { font-family: "Montserrat", sans-serif; font-weight: 400; fill: var(--white); }
  .tagline-small { font-family: "Montserrat", sans-serif; font-weight: 700; fill: var(--white); }
  .tagline-big { font-family: "Bodoni Moda", serif; font-weight: 500; fill: var(--white); }
</style>
</head>
<body>
<main class="canvas">

  <!-- 1080 x 1920 story ad -->
  <svg class="ad ad--story" viewBox="0 0 1080 1920" xmlns="http://www.w3.org/2000/svg">
    <defs>
      <clipPath id="story-frame"><rect width="1080" height="1920"/></clipPath>
      <radialGradient id="story-photo" cx="45%" cy="45%" r="60%">
        <stop offset="0" stop-color="var(--photo-warm)"/>
        <stop offset=".65" stop-color="var(--photo-deep)"/>
        <stop offset="1" stop-color="var(--photo-light)"/>
      </radialGradient>
    </defs>
    <g clip-path="url(#story-frame)">
      <rect class="ad__bg" width="1080" height="1920"/>
      <circle class="ad__line" cx="600" cy="560" r="480"/>
      <circle class="ad__line" cx="1180" cy="1400" r="700"/>
      <circle class="ad__line" cx="989" cy="77" r="152" style="opacity:0"/>
      <circle class="ad__dot" cx="989" cy="77" r="152"/>
      <circle class="ad__dot" cx="76" cy="1849" r="124"/>

      <text class="brand-name" x="540" y="232" font-size="150" text-anchor="middle">LUNETTE</text>

      <text class="headline" x="540" y="454" font-size="106" text-anchor="middle" textLength="634" lengthAdjust="spacingAndGlyphs">MACARONS</text>
      <text class="subline" x="540" y="528" font-size="58" text-anchor="middle" textLength="638" lengthAdjust="spacingAndGlyphs">Our products delight</text>

      <circle class="ad__ring" cx="539" cy="1067" r="438"/>
      <circle cx="539" cy="1063" r="411" fill="url(#story-photo)" role="img" aria-label="Photo of mango and yuzu macarons on crumpled baking paper"/>
      <circle class="ad__dot" cx="855" cy="1350" r="92"/>

      <text class="tagline-small" x="228" y="1764" font-size="58" textLength="186" lengthAdjust="spacingAndGlyphs">EVERY</text>
      <text class="tagline-small" x="228" y="1808" font-size="44" textLength="186" lengthAdjust="spacingAndGlyphs">BITE IS A</text>
      <text class="tagline-big" x="445" y="1808" font-size="122" textLength="407" lengthAdjust="spacingAndGlyphs">DREAM!</text>
    </g>
  </svg>

  <!-- 1080 x 1350 portrait ad -->
  <svg class="ad ad--portrait" viewBox="0 0 1080 1350" xmlns="http://www.w3.org/2000/svg">
    <defs>
      <clipPath id="portrait-frame"><rect width="1080" height="1350"/></clipPath>
      <radialGradient id="portrait-photo" cx="45%" cy="45%" r="60%">
        <stop offset="0" stop-color="var(--photo-warm)"/>
        <stop offset=".65" stop-color="var(--photo-deep)"/>
        <stop offset="1" stop-color="var(--photo-light)"/>
      </radialGradient>
    </defs>
    <g clip-path="url(#portrait-frame)">
      <rect class="ad__bg" width="1080" height="1350"/>
      <circle class="ad__line" cx="620" cy="420" r="460"/>
      <circle class="ad__line" cx="1120" cy="1150" r="600"/>
      <circle class="ad__dot" cx="987" cy="109" r="127"/>
      <circle class="ad__dot" cx="98" cy="1253" r="117"/>

      <text class="brand-name" x="540" y="201" font-size="132" text-anchor="middle">LUNETTE</text>

      <text class="headline" x="540" y="384" font-size="86" text-anchor="middle" textLength="507" lengthAdjust="spacingAndGlyphs">MACARONS</text>
      <text class="subline" x="540" y="442" font-size="47" text-anchor="middle" textLength="507" lengthAdjust="spacingAndGlyphs">Our products delight</text>

      <circle class="ad__ring" cx="540" cy="784" r="300"/>
      <circle cx="540" cy="773" r="283" fill="url(#portrait-photo)" role="img" aria-label="Photo of mango and yuzu macarons on crumpled baking paper"/>
      <circle class="ad__dot" cx="757" cy="977" r="63"/>

      <text class="tagline-small" x="229" y="1192" font-size="54" textLength="186" lengthAdjust="spacingAndGlyphs">EVERY</text>
      <text class="tagline-small" x="229" y="1239" font-size="42" textLength="186" lengthAdjust="spacingAndGlyphs">BITE IS A</text>
      <text class="tagline-big" x="446" y="1239" font-size="118" textLength="402" lengthAdjust="spacingAndGlyphs">DREAM!</text>
    </g>
  </svg>

</main>
</body>
</html>
```